Business Card Design

I am a Building Surveyor and run my own Building Consultat company, providing professional advice and services to builders, architects, designers, owners, etc.

Industry/Entity Type

Business

Contact Information for Business Card

Dorwen Fasque BBldgSurv (Hons)
Managing Director

47 Marlow Crest, Kelvoth Downs WA 6158
Mobile 0498 153 607
Email Dorwen.fasque@ridgeplumbav.com

Requirements
Must have
• I would like the back of the business card to be one colour (a shade of either black or maroon, matching the colours of my logo). Positioned in the centre on the back of the business card is to be my logo.

The front of the card is to be white, with my contact information in either black or maroon. The ADBldgSurv after my name should be in a smaller font size than my name. I would also like a small logo somewhere on this side of the card.

```html
<!DOCTYPE html>
<html lang="en">
<head>
<meta charset="utf-8">
<title>Kelvane Building Consultants — Business Card</title>
<link href="https://fonts.googleapis.com/css2?family=Quicksand:wght@400;500;600&display=swap" rel="stylesheet">
<style>
  :root {
    --page: #d9d9d9;
    --card-white: #fbfaf8;
    --card-black: #0b0b0b;
    --maroon: #7a1f1a;
    --maroon-soft: #a0443c;
    --grey-text: #6a6a6a;
    --faint: #ece8e6;
  }
  * { margin: 0; padding: 0; box-sizing: border-box; }
  html, body { width: 1200px; height: 1200px; overflow: hidden; }
  body {
    background: var(--page);
    font-family: "Quicksand", sans-serif;
    position: relative;
  }
  .card {
    position: absolute;
    left: 250px;
    width: 700px;
    height: 400px;
    border-radius: 4px;
    box-shadow: 0 8px 24px rgba(0,0,0,0.18);
    overflow: hidden;
  }
  .card-front { top: 150px; background: var(--card-white); }
  .card-back { top: 650px; background: var(--card-black); }

  .brand-small {
    position: absolute;
    left: 40px;
    top: 36px;
    display: flex;
    align-items: center;
    gap: 12px;
  }
  .brand-dot {
    width: 34px; height: 34px;
    border-radius: 50%;
    background: var(--maroon);
  }
  .brand-name {
    color: var(--maroon);
    font-weight: 600;
    font-size: 22px;
    letter-spacing: 1px;
    line-height: 1.05;
    text-transform: uppercase;
  }
  .brand-name small {
    display: block;
    font-size: 10px;
    letter-spacing: 2px;
    font-weight: 600;
  }
  .faint-circle {
    position: absolute;
    left: 105px;
    top: 110px;
    width: 230px;
    height: 230px;
    border-radius: 50%;
    border: 14px solid var(--faint);
  }
  .person {
    position: absolute;
    right: 44px;
    top: 92px;
    text-align: right;
  }
  .person-name {
    color: var(--maroon);
    font-size: 34px;
    font-weight: 500;
  }
  .person-title {
    color: var(--maroon);
    font-size: 12px;
    margin-top: 2px;
    padding-top: 4px;
    border-top: 1px solid var(--maroon-soft);
    display: inline-block;
  }
  .contact {
    position: absolute;
    left: 370px;
    top: 235px;
    list-style: none;
    color: var(--maroon);
    font-size: 15px;
    letter-spacing: 2px;
  }
  .contact li {
    display: flex;
    align-items: flex-start;
    gap: 14px;
    margin-bottom: 12px;
  }
  .contact svg { flex: none; width: 16px; height: 16px; margin-top: 2px; }
  .contact .email { font-size: 13px; letter-spacing: 1px; }

  .brand-large {
    position: absolute;
    left: 50%; top: 50%;
    transform: translate(-50%, -50%);
    display: flex;
    align-items: center;
    gap: 18px;
  }
  .brand-large .brand-dot { width: 58px; height: 58px; background: var(--maroon); }
  .brand-large .brand-name {
    color: var(--grey-text);
    font-size: 38px;
  }
  .brand-large .brand-name small { font-size: 15px; letter-spacing: 3px; }
</style>
</head>
<body>
  <section class="card card-front" aria-label="Card front">
    <div class="brand-small">
      <span class="brand-dot"></span>
      <div class="brand-name">Kelvane<small>Building Consultants</small></div>
    </div>
    <div class="faint-circle" aria-hidden="true"></div>
    <div class="person">
      <div class="person-name">Dorwen Fasque</div>
      <div class="person-title">ADBldgSurv Director</div>
    </div>
    <ul class="contact">
      <li>
        <svg viewBox="0 0 16 16" aria-hidden="true"><path d="M2 8 L8 2 L14 8 M4 7 V14 H12 V7" fill="none" stroke="currentColor" stroke-width="1.6"/></svg>
        <span>47 Marlow Crest, Kelvoth Downs<br>WA 6158</span>
      </li>
      <li>
        <svg viewBox="0 0 16 16" aria-hidden="true"><rect x="4" y="1" width="8" height="14" rx="1.5" fill="none" stroke="currentColor" stroke-width="1.6"/><circle cx="8" cy="12" r="1" fill="currentColor"/></svg>
        <span>0498 153 607</span>
      </li>
      <li>
        <svg viewBox="0 0 16 16" aria-hidden="true"><rect x="1" y="3" width="14" height="10" fill="none" stroke="currentColor" stroke-width="1.6"/><path d="M1 3 L8 9 L15 3" fill="none" stroke="currentColor" stroke-width="1.6"/></svg>
        <span class="email">Dorwen.fasque@ridgeplumbav.com</span>
      </li>
    </ul>
  </section>

  <section class="card card-back" aria-label="Card back">
    <div class="brand-large">
      <span class="brand-dot"></span>
      <div class="brand-name">Kelvane<small>Building Consultants</small></div>
    </div>
  </section>
</body>
</html>
```